Craft Beer and Sausage Bar Cluttered look

The Bar carries only local beers from Kegs and given as draft beers. The design needs to be dedicated towards the young crowd, and yes, we would like a more cluttered and different look. I have included the symbol and the logo to improve the idea. We will be having a 360 view of the locations, high end photos, and many images we can add into a galleries section. The main focus needs to be the initial vision that a user gets as soon as they look at the landing page.

Ive received several queries about one question and I'd like to clarify...

Just a psd for the home page will be fine, i have my own team that can convert it to a responsive html and into a site. and here are some more pics...
https://www.filevanto.com/sh/kx82pq1wm7zr4ta/QQtrnbLpWoejvYx-MuplaRs?dl=0

Target Market(s)

21 to 40 year old crowd

Industry/Entity Type

Crowd

Number of Pages Required

1 page

Other font styles liked:
• chalkboard and rough look, tattoo styles

Requirements
Must have
• Focus on Craft Beer and cluttered look, we will have many locations of the locations, already up to 3 locations and a food truck, and is growing another two locations in just another month., to show you the design of the truck, ive included that in the attached and its ONLY YO GIVE THE IDEA
Nice to have
• Something different, should portray the image of local brews are being served
• Some examples they liked...
• http://www.merriwellkinfolk.com
• (Rebranded for Beer of course) http://www.tovrunk.com
• http://www.plumtreeleafden.com/
• http://www.fenn-wacker.de/
• http://orlenlanezapfhaus.com/
• https://www.quillrovers.com/
• http://theplumwickery.com/
Should not have
• No standard slider at the top, etc. should not look like a chain, nor family place. needs to be for the younger dating crowd

```html
<!DOCTYPE html>
<html lang="en">
<head>
<meta charset="utf-8">
<title>Halden Brook Kitchen &amp; Taps</title>
<link rel="stylesheet" href="https://fonts.googleapis.com/css2?family=Open+Sans:wght@400;600;700&display=swap">
<style>
  :root {
    --red: #e3141c;
    --ink: #0d0b0b;
    --panel: rgba(12, 8, 8, 0.82);
    --white: #ffffff;
    --muted: #cfcfcf;
    --footer: #111010;
    --rule: #3a3a3a;
  }
  * { box-sizing: border-box; margin: 0; padding: 0; }
  html, body { width: 820px; height: 1200px; overflow: hidden; }
  body {
    position: relative;
    font-family: "Open Sans", Arial, sans-serif;
    color: var(--white);
    background: var(--ink);
  }
  .backdrop {
    position: absolute; left: 0; top: 0; width: 820px; height: 1010px;
    background:
      radial-gradient(ellipse at 88% 88%, rgba(227,20,28,0.95) 0%, rgba(227,20,28,0) 45%),
      radial-gradient(ellipse at 10% 92%, rgba(200,16,24,0.85) 0%, rgba(200,16,24,0) 40%),
      radial-gradient(ellipse at 30% 20%, #6b3a2c 0%, rgba(107,58,44,0) 55%),
      linear-gradient(180deg, #3a2620 0%, #5a2a22 35%, #7a1c18 70%, #9b1116 100%);
  }
  .site-header { position: absolute; left: 0; top: 0; width: 820px; height: 70px; }
  .brand {
    position: absolute; left: 108px; top: 16px;
    font-weight: 700; font-size: 17px; line-height: 19px; color: var(--white);
  }
  .main-nav {
    position: absolute; right: 112px; top: 42px;
    display: flex; gap: 22px;
  }
  .main-nav a {
    color: var(--white); text-decoration: none;
    font-size: 10px; font-weight: 600; letter-spacing: 0.3px;
  }
  .main-nav a.is-active { color: var(--red); }

  .concept-panel {
    position: absolute; left: 108px; top: 180px; width: 604px; height: 300px;
    background: var(--panel);
    padding: 22px 36px; text-align: center;
  }
  .panel-title { color: var(--red); font-size: 21px; font-weight: 600; letter-spacing: 1px; line-height: 26px; }
  .panel-lead { font-size: 11.5px; font-weight: 700; margin-top: 2px; }
  .panel-copy { font-size: 9.5px; line-height: 13px; color: var(--muted); margin-top: 4px; }
  .panel-title.why { margin-top: 22px; }

  .daily-heading {
    position: absolute; left: 0; width: 820px; top: 516px;
    text-align: center; font-size: 27px; font-weight: 600;
  }
  .daily-heading .accent { color: var(--red); }

  .daily-cards {
    position: absolute; left: 108px; top: 568px; width: 604px;
    display: flex; gap: 8px;
  }
  .card { width: 196px; }
  .card-photo { height: 148px; border: 1px solid #222; }
  .card-photo.bar { background: linear-gradient(160deg, #4a3a30, #1e1612 70%, #5a2a20); }
  .card-photo.crowd { background: linear-gradient(160deg, #6a5040, #2a1c16 60%, #7a4a30); }
  .card-photo.taps { background: linear-gradient(160deg, #5a4a40, #241a16 60%, #3a2a22); }
  .card-text {
    background: var(--panel); height: 100px; margin-top: 8px;
    padding: 8px; font-size: 10.5px; line-height: 13px;
  }
  .see-more {
    display: block; width: 56px; height: 18px; margin: 10px auto 0;
    background: var(--red); color: var(--white); text-decoration: none;
    font-size: 8.5px; font-weight: 700; text-align: center; line-height: 18px;
  }

  .site-footer {
    position: absolute; left: 0; top: 1010px; width: 820px; height: 190px;
    background: var(--footer);
  }
  .footer-brand {
    position: absolute; left: 100px; top: 72px;
    font-weight: 700; font-size: 14px; line-height: 16px; color: var(--white);
  }
  .link-col { position: absolute; top: 30px; width: 150px; }
  .link-col.first { left: 288px; }
  .link-col.second { left: 480px; }
  .link-col h3 {
    font-size: 10px; font-weight: 600; padding-bottom: 10px;
    border-bottom: 1px solid var(--rule);
  }
  .link-col ul { list-style: none; margin-top: 10px; }
  .link-col li { font-size: 9.5px; line-height: 19px; color: var(--muted); }
  .social { position: absolute; left: 604px; top: 114px; display: flex; gap: 14px; }
  .social span { width: 14px; height: 14px; border-radius: 50%; background: var(--white); }
  .copyright {
    position: absolute; left: 100px; top: 164px;
    font-size: 9px; color: var(--muted);
  }
</style>
</head>
<body>
  <div class="backdrop" role="img" aria-label="Photo of the bar: red-lit brick walls and beer taps"></div>

  <header class="site-header">
    <div class="brand">Halden Brook<br>Kitchen &amp; Taps</div>
    <nav class="main-nav">
      <a href="#">HOME</a>
      <a href="#" class="is-active">OUR BEER</a>
      <a href="#">ABOUT US</a>
      <a href="#">CONTACT US</a>
    </nav>
  </header>

  <section class="concept-panel">
    <h2 class="panel-title">CONCEPT</h2>
    <p class="panel-lead">A Great Blend Of Old World Traditions And Today's Cool</p>
    <p class="panel-copy">Our place is the local gathering spot where craft beer from nearby brewers meets hand-made sausages and good company. Every tap pours a keg from just down the road, served fresh in a room built for long talks.</p>
    <h2 class="panel-title why">WHY</h2>
    <p class="panel-copy">The beer scene has grown up, and so has its crowd. We pour only local drafts, rotate the taps weekly and keep the kitchen open late, so every visit feels new. Bring friends, meet new ones and find your next favourite brew at the bar.</p>
    <p class="panel-copy">Three locations and a food truck, with two more opening soon.</p>
    <p class="panel-copy">Follow the truck and find the nearest tap.</p>
  </section>

  <h2 class="daily-heading"><span class="accent">Beer</span> Food &amp; Fun Served Up daily</h2>

  <section class="daily-cards">
    <article class="card">
      <div class="card-photo bar" role="img" aria-label="Photo of the bar counter at night"></div>
      <p class="card-text">Imagine your exhausted from a long day at work. Before heading Home you decide to meet your friends at what see place everyone's talking about.</p>
      <a href="#" class="see-more">See More</a>
    </article>
    <article class="card">
      <div class="card-photo crowd" role="img" aria-label="Photo of a busy dining room"></div>
      <p class="card-text">Within a few short minutes your taste buds are dancing! The Giant Pretzel is the first to arrive, over 18inches and served with beer cheese sauce.</p>
      <a href="#" class="see-more">See More</a>
    </article>
    <article class="card">
      <div class="card-photo taps" role="img" aria-label="Photo of the tap wall"></div>
      <p class="card-text">The Giant Pretzel is the first to arrive, over 18inches and served with beer cheese sauce.</p>
      <a href="#" class="see-more">See More</a>
    </article>
  </section>

  <footer class="site-footer">
    <div class="footer-brand">Halden Brook<br>Kitchen &amp; Taps</div>
    <div class="link-col first">
      <h3>Quick Links</h3>
      <ul><li>Our Products</li><li>Our Purpose</li><li>Shop</li></ul>
    </div>
    <div class="link-col second">
      <h3>Quick Links</h3>
      <ul><li>Contact Us</li><li>Privacy Policy</li><li>Terms of Use</li></ul>
    </div>
    <div class="social" aria-label="Social links">
      <span></span><span></span><span></span><span></span>
    </div>
    <p class="copyright">Halden Brook Kitchen &amp; Taps All rights reserved</p>
  </footer>
</body>
</html>
```